Australian Raw Honey Label Design for Florvane Honey

We need a new label design for our honey jars. Previous label was very amateurish and we need a new more professional look. We are also changing name to Florvane; which means kiss in French. The label should be simple, fluid, with simple drawings of flowers, bees in the décor reflecting the minimal process we use in producing our honey.
I would like to use my profile (curly/afro hair) (that people can recognise ) that connects with bees. The colour scheme should be warm sun, yellow or orange without too many colours or heavy background.

Label size: 200 mm x 60 mm
there are two variantes of the label, one with 1kg and the other with 500g
More information in the attached brief.

Target Market(s)

customer looking for locally produced honey vs commercial supermarket honey. Product sold mostly through word of mouth

Colors
ffc214
f78f20
f68e4e
fbed22

Requirements
Must have
• Included in the brief as per food label requirement
Nice to have
• curve, flowy font for brand name
• Brand means kiss, so connection with bees is important.
Should not have
• heavy background colors

```html
<!DOCTYPE html>
<html lang="en">
<head>
<meta charset="utf-8">
<title>Florvane Premium Raw Honey – 500g label</title>
<link href="https://fonts.googleapis.com/css2?family=Roboto:wght@400;500&family=Yanone+Kaffeesatz:wght@400;500&display=swap" rel="stylesheet">
<style>
  :root {
    --label-yellow: #fec52b;
    --sun-glow: #fbed22;
    --ink: #6a4a2c;
    --brand-brown: #8c4a26;
    --rule: #8a5a2a;
    --table-ink: #7a4a22;
    --bullet: #c98a1e;
    --art-warm: #e3a233;
  }
  * { box-sizing: border-box; margin: 0; padding: 0; }
  html, body { width: 1200px; height: 385px; overflow: hidden; }
  body { background: var(--label-yellow); font-family: "Roboto", Arial, sans-serif; color: var(--ink); }

  .label { position: relative; width: 1200px; height: 385px; background: var(--label-yellow); overflow: hidden; }

  .bullet { display: inline-block; width: 17px; height: 17px; border-radius: 50%; background: var(--bullet); vertical-align: -2px; margin-right: 6px; }

  /* Story column */
  .story { position: absolute; left: 37px; top: 40px; width: 261px; font-size: 15.6px; line-height: 20.2px; text-align: justify; }
  .story .brand-inline { font-family: "Yanone Kaffeesatz", "Arial Narrow", sans-serif; font-size: 18px; color: var(--brand-brown); letter-spacing: .5px; }
  .contact { position: absolute; left: 37px; top: 282px; font-size: 15.6px; line-height: 20px; }
  .contact h3, .info h3 { font-weight: 400; font-size: 15.6px; }
  .contact p { padding-left: 24px; }

  /* Centre brand panel */
  .glow { position: absolute; left: 330px; top: 40px; width: 340px; height: 320px; background: radial-gradient(circle at 50% 58%, var(--sun-glow) 0%, rgba(251,237,34,.6) 35%, rgba(254,197,43,0) 68%); }
  .brand { position: absolute; left: 330px; width: 340px; text-align: center; color: var(--brand-brown); font-family: "Yanone Kaffeesatz", "Arial Narrow", sans-serif; }
  .brand-name { top: 36px; font-size: 44px; letter-spacing: 3px; font-weight: 400; }
  .brand-tagline { top: 86px; font-size: 27px; letter-spacing: 1.5px; font-weight: 400; }
  .portrait-art { position: absolute; left: 360px; top: 128px; width: 245px; height: 208px; border-radius: 48% 52% 40% 44%; background: radial-gradient(ellipse at 50% 45%, rgba(227,162,51,.55), rgba(227,162,51,.15) 70%, rgba(227,162,51,0)); }

  .weight-rule { position: absolute; left: 0; right: 0; top: 350px; height: 1px; }
  .weight-rule::before, .weight-rule::after { content: ""; position: absolute; top: 0; height: 1px; background: var(--rule); }
  .weight-rule::before { left: 0; width: 428px; }
  .weight-rule::after { left: 508px; right: 0; }
  .weight { position: absolute; left: 428px; width: 80px; top: 337px; text-align: center; font-size: 21px; color: var(--ink); }

  /* Info column */
  .info { position: absolute; left: 640px; top: 40px; width: 295px; font-size: 15.6px; line-height: 19.7px; }
  .info section { margin-bottom: 5px; }
  .info p { padding-left: 23px; }
  .info .justified { text-align: justify; width: 272px; margin-top: 8px; }
  .bee-art { position: absolute; left: 893px; top: 40px; width: 36px; height: 30px; border-radius: 50%; background: var(--art-warm); }
  .origin-badge { position: absolute; left: 880px; top: 258px; width: 52px; height: 70px; border-radius: 4px; background: #fff; border: 2px solid #2e8a3e; }

  /* Nutrition table */
  .nutrition { position: absolute; left: 953px; top: 40px; width: 207px; height: 289px; border: 1px solid var(--rule); color: var(--table-ink); font-size: 9.3px; }
  .nutrition h2 { font-weight: 400; font-size: 13.4px; text-align: center; padding: 10px 0 4px; }
  .nutrition .meta { padding: 3px 6px 6px; border-bottom: 1px solid var(--rule); }
  .nutrition .meta:first-of-type { border-bottom: none; padding-bottom: 2px; }
  .serving-head { display: grid; grid-template-columns: 80px 62px 63px; height: 69px; border-bottom: 1px solid var(--rule); align-items: center; }
  .dipper-art { width: 60px; height: 56px; margin-left: 10px; border-radius: 30% 30% 50% 50%; background: linear-gradient(160deg, rgba(227,162,51,.4), rgba(227,162,51,.8)); }
  .serving-head span { line-height: 11px; }
  .nutrition table { width: 100%; border-collapse: collapse; }
  .nutrition td { height: 21.3px; padding: 0 6px; border-bottom: 1px solid var(--rule); }
  .nutrition tr:last-child td { border-bottom: none; }
  .nutrition td.num { text-align: right; }
</style>
</head>
<body>
<main class="label">

  <p class="story"><span class="bullet"></span><span class="brand-inline">FLORVANE</span> (meaning kiss in French) is raw, natural honey made with love by our happy bees. They are foraging on a rich mixture of suburban flora from Ashbrook Vale. Unlike commercial honey which is often pasteurised, our raw honey is not heated which helps preserve the flavour and natural benefits of locally produced honey.</p>

  <div class="contact">
    <h3><span class="bullet"></span>Contact us:</h3>
    <p>hello@florvanehoney.com.au</p>
    <p>04 55 210 638</p>
  </div>

  <div class="glow"></div>
  <h1 class="brand brand-name">FLORVANE</h1>
  <p class="brand brand-tagline">PREMIUM RAW HONEY</p>
  <div class="portrait-art" role="img" aria-label="Line illustration of a woman's profile whose curly hair is made of a swarm of bees"></div>

  <div class="weight-rule"></div>
  <p class="weight">500g</p>

  <div class="info">
    <section>
      <h3><span class="bullet"></span>Storage instructions:</h3>
      <p>Store in a cool, dry place.</p>
      <p class="justified">Crystallisation is a normal process that happens overtime. This does not alter the quality of the honey. The process can be reversed by placing the container in hot water (no more than 45°C) and letting it stand until completely liquefied.</p>
    </section>
    <section>
      <h3><span class="bullet"></span>Ingredient list:</h3>
      <p>100% pure Australian honey</p>
    </section>
    <section>
      <h3><span class="bullet"></span>Batch code:</h3>
    </section>
  </div>
  <div class="bee-art" role="img" aria-label="Small drawing of a flying bee"></div>
  <div class="origin-badge" role="img" aria-label="Country of origin badge"></div>

  <div class="nutrition">
    <h2>Nutritional information</h2>
    <p class="meta">Servings per package: 25</p>
    <p class="meta">Serving size: 20g</p>
    <div class="serving-head">
      <div class="dipper-art" role="img" aria-label="Drawing of a honey dipper dripping honey"></div>
      <span>Average Quantity per Serving</span>
      <span>Average Quantity per 100 g</span>
    </div>
    <table>
      <tr><td>Energy</td><td class="num">280 kJ</td><td class="num">1400 kJ</td></tr>
      <tr><td>Protein</td><td class="num">0.0 g</td><td class="num">0.2 g</td></tr>
      <tr><td>Fat, total</td><td class="num">0.0 g</td><td class="num">0.0 g</td></tr>
      <tr><td>-saturated</td><td class="num">0.0 g</td><td class="num">0.0 g</td></tr>
      <tr><td>Carbohydrate</td><td class="num">16.4 g</td><td class="num">82.1 g</td></tr>
      <tr><td>-sugars</td><td class="num">16.4 g</td><td class="num">82.1 g</td></tr>
      <tr><td>Sodium</td><td class="num">3 mg</td><td class="num">14 mg</td></tr>
    </table>
  </div>

</main>
</body>
</html>
```